Daniel Pruitt for Honest & Open Harlow County

Design website with same functions and similar concept, the news section would be plugged in the a section that shows timelines years 'dates over a 20 year period with little picture and short descriptions of key events. The website will need to be fully functional with the donation link tied to paypal. I already have the website registered just need the page tied to the URL and will need Link to facebook page. Wordpress or a design that is compatible with Google hosting

https://www.brennick-ovale.com/
Updates

The logo at the top similar to the website link attached should say Daniel Pruitt for Harlow County

Coding

Coded - Design and coding required

Number of Pages Required

1 page

Requirements
Nice to have
• Just updated the design with some photos of me deployed to Afghanistan in 2011-2012 and once from deployment to Iraq 2006-2008(the one walking down the street) to use for the timeline. Also update is a photo of our family and a photo of my wife and I in high school as we’ve been high school sweethearts sense since 1999 more than 20 years. The picture of kids lined up for kids from Afghanistan that in my squad organized a clothing and shoe drive organized me for local kids to obtain winter clothing items and coats and shoes. Please don’t use all the military photos just one to highlight my military service, you can just fill in a template with generic info I’ll provide the text once the design is finalized. Same for the family photo. I am married to my high school sweetheart Megan. We have three boys Trevor 14, Owen nine, and Bradley three. We’ve been residence of Harlow county since I was medically retired from the military In 2015. Wanted to provide some photos in order to make it more personalized, these photos are by no means the final ones, so Porvided some more personal info to tailor the text it’s not necessary but a designer that is creative with text and understands what should be there for the description is beneficial but not necessary for me. If you receive w still in the running message please make what updates you can and resubmit!! The ability to work quickly and seemlessly to personalize the design will be important. Thank y’all!! Good luck!! Would also like to see the mobile example of the platform if you have that available.

```html
<!DOCTYPE html>
<html lang="en">
<head>
<meta charset="utf-8">
<title>Daniel Pruitt for Harlow County</title>
<link href="https://fonts.googleapis.com/css2?family=Alegreya+Sans:wght@500;700;800&family=Barlow+Condensed:wght@500;600&family=Montserrat:wght@400;500;700&family=Work+Sans:wght@400;600;700&display=swap" rel="stylesheet">
<style>
:root{
  --blue:#1a5889;
  --blue-dark:#174f7c;
  --red:#c62026;
  --card:#f1f3f6;
  --ink:#3a3a3a;
  --white:#ffffff;
}
*{box-sizing:border-box;margin:0;padding:0}
html,body{width:1200px;height:3647px;overflow:hidden;background:var(--white)}
body{font-family:"Montserrat",sans-serif;color:var(--ink)}
.page{position:relative;width:1200px;height:3647px;overflow:hidden}
.abs{position:absolute}

/* top strip */
.topline{top:15px;right:51px;font:700 10px "Work Sans",sans-serif;color:var(--blue);letter-spacing:.2px;text-transform:uppercase}
.topline span{color:var(--red)}

/* hero */
.hero{top:44px;left:0;width:1200px;height:560px;
  background:linear-gradient(180deg,#5d8fd8 0%,#7aa2e0 38%,#a99482 62%,#8a6a55 78%,#5d7a4a 100%)}
.hero-person{top:60px;left:555px;width:500px;height:544px;
  background:linear-gradient(180deg,#c9a48c 0%,#8eb8e8 35%,#6fa0d8 100%);border-radius:220px 220px 0 0;opacity:.85}
.logo-box{top:0;left:50px;width:208px;height:173px;background:var(--blue);display:flex;align-items:center;justify-content:center}
.logo-card{width:155px;height:140px;background:var(--white);display:flex;flex-direction:column;align-items:center;justify-content:center;text-align:center;font:700 19px/1.1 "Alegreya Sans",sans-serif;color:var(--blue);padding:8px}
.logo-card small{font-size:12px;margin-top:6px}
.nav{top:78px;left:404px;display:flex;gap:32px}
.nav a{font:500 27px "Barlow Condensed",sans-serif;color:var(--white);text-decoration:none;text-transform:uppercase}
.btn-donate-top{top:68px;left:1006px;width:143px;height:49px;background:var(--red);color:var(--white);font:700 16px "Work Sans",sans-serif;display:flex;align-items:center;justify-content:center;letter-spacing:1px}

.signup{top:215px;left:0;width:458px;height:277px;background:var(--white)}
.signup h2{position:absolute;top:26px;left:50px;font:700 27px "Alegreya Sans",sans-serif;color:var(--blue)}
.field{position:absolute;height:42px;border:1px solid #b7b7b7;font:600 14px "Work Sans",sans-serif;color:var(--blue);padding:12px 16px}
.signup .join{position:absolute;top:193px;left:50px;width:376px;height:42px;background:var(--red);color:var(--white);font:600 14px "Work Sans",sans-serif;display:flex;align-items:center;justify-content:center}

/* support band */
.support{top:604px;left:0;width:1200px;height:156px;background:var(--red)}
.support .kicker{position:absolute;top:40px;left:156px;font:700 16px "Work Sans",sans-serif;color:var(--white)}
.support h2{position:absolute;top:62px;left:151px;font:700 33px "Work Sans",sans-serif;color:var(--white);letter-spacing:.5px}
.amount{position:absolute;top:60px;width:100px;height:42px;border:2px solid var(--white);color:var(--white);font:700 17px "Work Sans",sans-serif;display:flex;align-items:center;justify-content:center}
.support .donate{position:absolute;top:60px;left:961px;width:188px;height:42px;background:var(--blue);color:var(--white);font:700 17px "Work Sans",sans-serif;letter-spacing:1px;display:flex;align-items:center;justify-content:center}

/* action cards */
.card{top:808px;width:360px;height:211px;background:var(--card);text-align:center}
.card h3{margin-top:26px;font:800 28px "Alegreya Sans",sans-serif;color:var(--blue)}
.card p{margin:6px auto 0;width:310px;font:400 17px/21px "Work Sans",sans-serif;color:#444}
.card .btn{position:absolute;top:123px;left:73px;width:214px;height:42px;background:var(--blue);color:var(--white);font:600 16px "Work Sans",sans-serif;letter-spacing:1px;display:flex;align-items:center;justify-content:center}

/* about */
.about-kicker{top:1112px;left:50px;font:700 16px "Alegreya Sans",sans-serif;color:var(--red)}
.about-title{top:1143px;left:50px;font:500 34px/46px "Alegreya Sans",sans-serif;color:var(--blue)}
.body-copy{font:400 17px/23.5px "Lato","Montserrat",sans-serif;color:#555}
.about-copy{top:1252px;left:50px;width:545px}
.btn-blue{background:var(--blue);color:var(--white);font:700 16px "Work Sans",sans-serif;display:flex;align-items:center;justify-content:center}
.about-btn{top:1400px;left:50px;width:154px;height:43px}
.photo{background:linear-gradient(135deg,#d8d2c8,#9a8f80);}
.about-photo{top:1115px;left:696px;width:453px;height:328px}

/* media timeline */
.media-title{top:1583px;left:0;width:1200px;text-align:center;font:700 27px "Alegreya Sans",sans-serif;color:var(--blue)}
.axis{top:2227px;left:0;width:1200px;height:4px;background:var(--blue)}
.year{top:2212px;width:82px;height:36px;background:var(--red);color:var(--white);font:700 16px "Work Sans",sans-serif;display:flex;align-items:center;justify-content:center}
.stem{width:3px;background:var(--red)}
.stem.blue{background:var(--blue)}
.tl-note{font:400 14.5px/16.4px "Montserrat",sans-serif;color:#222}
.tl-note .tag{display:block;font-size:14.5px;color:var(--red);margin-bottom:5px}
.tl-note.r{text-align:right}
.tl-photo{background:linear-gradient(135deg,#7c9a6a,#d9dad6 60%,#3a4d7a)}
.badge{top:1835px;left:143px;width:44px;height:114px;background:var(--blue)}
.rot{transform:rotate(-90deg);transform-origin:center;white-space:nowrap;display:flex;align-items:center;justify-content:center}

/* delivered */
.deliv-title{top:2437px;left:54px;font:700 35px/47px "Alegreya Sans",sans-serif;color:var(--blue)}
.deliv-copy{top:2549px;left:54px;width:590px}
.btn-pill{top:2715px;left:55px;width:193px;height:50px;border-radius:25px;background:var(--red);color:var(--white);font:700 16px "Work Sans",sans-serif;display:flex;align-items:center;justify-content:center}
.deliv-photo{top:2462px;left:698px;width:451px;height:328px;background:linear-gradient(135deg,#e6e8ea,#8d96a2 60%,#3d434c)}

/* newsletter */
.news{top:2885px;left:0;width:1200px;height:125px;background:var(--red)}
.news .kicker{position:absolute;top:35px;left:89px;font:400 17px "Work Sans",sans-serif;color:var(--white)}
.news h2{position:absolute;top:58px;left:89px;font:700 25px "Alegreya Sans",sans-serif;color:var(--white)}
.pill{position:absolute;top:47px;height:44px;border-radius:22px;background:var(--white);font:400 17px "Work Sans",sans-serif;color:var(--blue);padding:11px 22px}
.news .sub{position:absolute;top:47px;left:968px;width:131px;height:44px;border-radius:22px;background:var(--blue);color:var(--white);font:500 14px "Work Sans",sans-serif;letter-spacing:.8px;display:flex;align-items:center;justify-content:center}

/* footer */
.footer{top:3010px;left:0;width:1200px;height:637px;background:var(--blue)}
.foot-logo{top:79px;left:528px;width:146px;height:126px;background:var(--white);display:flex;flex-direction:column;align-items:center;justify-content:center;text-align:center;font:700 19px/1.1 "Alegreya Sans",sans-serif;color:var(--blue)}
.foot-logo small{font-size:12px;margin-top:5px}
.foot-nav{top:280px;left:0;width:1200px;display:flex;justify-content:center;gap:33px}
.foot-nav a{font:500 27px "Barlow Condensed",sans-serif;color:var(--white);text-decoration:none;text-transform:uppercase}
.socials{top:340px;left:541px;display:flex;gap:22px}
.socials span{width:24px;height:24px;border-radius:50%;background:var(--white)}
.paid{top:392px;left:482px;width:237px;height:35px;border:2px solid var(--white);color:var(--white);font:700 9.5px "Work Sans",sans-serif;display:flex;align-items:center;justify-content:center}
.fine{left:160px;width:880px;text-align:center;color:var(--white);font:400 9.5px/14px "Work Sans",sans-serif;text-transform:uppercase}
</style>
</head>
<body>
<div class="page">

  <p class="abs topline">Daniel Pruitt isn't taking corporate PAC contributions. He relies on people like you. <span>Donate</span></p>

  <section class="abs hero" role="img" aria-label="Candidate in a blue shirt giving a thumbs up in front of the county courthouse"></section>
  <div class="abs hero-person" role="img" aria-label="Portrait of the candidate"></div>

  <div class="abs logo-box"><div class="logo-card">Daniel Pruitt<small>for Harlow County</small></div></div>

  <nav class="abs nav">
    <a href="#">Home</a><a href="#">Meet Pruitt</a><a href="#">Endorse</a><a href="#">News</a><a href="#">Volunteer</a>
  </nav>
  <a class="abs btn-donate-top">DONATE</a>

  <form class="abs signup">
    <h2>I stand With Daniel Pruitt</h2>
    <div class="field" style="top:84px;left:50px;width:182px">First Name</div>
    <div class="field" style="top:84px;left:246px;width:180px">Last Name</div>
    <div class="field" style="top:139px;left:50px;width:182px">Email</div>
    <div class="field" style="top:139px;left:246px;width:180px">Phone</div>
    <div class="join">Join the Team</div>
  </form>

  <section class="abs support">
    <p class="kicker">Help Support</p>
    <h2>Our Campaign</h2>
    <div class="amount" style="left:482px">$25</div>
    <div class="amount" style="left:602px">$50</div>
    <div class="amount" style="left:721px">$100</div>
    <div class="amount" style="left:840px">$250</div>
    <div class="donate">DONATE</div>
  </section>

  <div class="abs card" style="left:50px">
    <h3>Endorse Pruitt</h3>
    <p>Join many others from across Harlow County in endorsing Pruitt.</p>
    <div class="btn">ADD YOUR NAME</div>
  </div>
  <div class="abs card" style="left:420px">
    <h3>Action Team</h3>
    <p>Get involved by signing up to volunteer for our campaign.</p>
    <div class="btn">TAKE ACTION</div>
  </div>
  <div class="abs card" style="left:788px">
    <h3>Election Day</h3>
    <p>Election Day is Tuesday, November 3rd. Learn more.</p>
    <div class="btn">POLLING LOCATIONS</div>
  </div>

  <p class="abs about-kicker">I'm Daniel Pruitt</p>
  <h2 class="abs about-title">Family Man. Businessman.<br>Decorated Veteran.</h2>
  <p class="abs body-copy about-copy">Ut enim ad minim veniam, quis nostrud exercitation ullamco laboris nisi ut aliquip ex ea commodo consequat. Duis aute irure dolor in reprehenderit in voluptate velit esse cillum dolore eu fugiat nulla pariatur. Excepteur sint occaecat cupidatat non proident, sunt in culpa qui officia deserunt mollit anim id est laborum.</p>
  <div class="abs btn-blue about-btn">READ MORE</div>
  <div class="abs photo about-photo" role="img" aria-label="Candidate with his family on the living room sofa"></div>

  <h2 class="abs media-title">Daniel Pruitt in media</h2>

  <div class="abs tl-note r" style="top:1677px;left:88px;width:174px"><span class="tag">dolore</span>Duis aute irure dolor in reprehenderit in voluptate velit esse cillum dolore eu fugiat nulla pariatur.</div>
  <div class="abs badge"><div class="rot" style="width:44px;height:114px;color:#fff;font:500 28px Montserrat,sans-serif">dolore</div></div>
  <div class="abs" style="top:1811px;left:198px;width:46px;height:145px"><div class="rot" style="width:46px;height:145px;color:var(--red);font:500 48px Montserrat,sans-serif">15000</div></div>
  <div class="abs stem" style="top:1807px;left:259px;height:405px"></div>

  <div class="abs tl-note r" style="top:1983px;left:24px;width:206px"><span class="tag">dolore</span>Duis aute irure dolor in reprehenderit in voluptate velit esse cillum dolore eu fugiat nulla pariatur.</div>
  <div class="abs stem" style="top:2080px;left:97px;height:132px"></div>

  <div class="abs tl-note" style="top:1999px;left:306px;width:232px"><span class="tag" style="margin-left:84px">dolore</span>Duis aute irure dolor in reprehenderit in voluptate velit esse cillum dolore eu fugiat nulla pariatur.</div>
  <div class="abs stem" style="top:2121px;left:428px;height:91px"></div>

  <div class="abs tl-note r" style="top:1721px;left:390px;width:212px"><span class="tag">dolore</span>Duis aute irure dolor in reprehenderit in voluptate velit esse cillum dolore eu fugiat nulla pariatur.</div>
  <div class="abs tl-photo" style="top:1840px;left:461px;width:141px;height:94px" role="img" aria-label="Candidate in a suit outdoors"></div>
  <div class="abs stem" style="top:1941px;left:599px;height:271px"></div>

  <div class="abs tl-note r" style="top:1990px;left:684px;width:146px"><span class="tag">dolore</span>Duis aute irure dolor in reprehenderit in voluptate velit esse cillum dolore eu fugiat nulla pariatur.</div>
  <div class="abs stem" style="top:2121px;left:767px;height:91px"></div>

  <div class="abs tl-note r" style="top:1667px;left:848px;width:146px"><span class="tag" style="text-align:left;margin-left:96px">dolore</span>Duis aute irure dolor in reprehenderit in voluptate velit esse cillum dolore eu fugiat nulla pariatur.</div>
  <div class="abs stem blue" style="top:1793px;left:936px;height:66px"></div>
  <div class="abs tl-photo" style="top:1882px;left:865px;width:141px;height:95px;background:linear-gradient(135deg,#f1ece4,#c9b9a3 55%,#2f3b58)" role="img" aria-label="Candidate meeting residents at a community event"></div>
  <div class="abs stem" style="top:2011px;left:934px;height:201px"></div>

  <div class="abs tl-note r" style="top:2042px;left:966px;width:196px"><span class="tag">dolore</span>Duis aute irure dolor in reprehenderit in voluptate velit esse cillum dolore eu fugiat nulla pariatur.</div>
  <div class="abs stem" style="top:2175px;left:1104px;height:37px"></div>

  <div class="abs axis"></div>
  <div class="abs year" style="left:51px">2015</div>
  <div class="abs year" style="left:219px">2016</div>
  <div class="abs year" style="left:389px">2017</div>
  <div class="abs year" style="left:558px">2018</div>
  <div class="abs year" style="left:727px">2019</div>
  <div class="abs year" style="left:897px">2020</div>
  <div class="abs year" style="left:1066px">2021</div>

  <h2 class="abs deliv-title">Daniel Pruitt Delivered When<br>Harlow County Needed It Most.</h2>
  <p class="abs body-copy deliv-copy">Ut enim ad minim veniam, quis nostrud exercitation ullamco laboris nisi ut aliquip ex ea commodo consequat. Duis aute irure dolor in reprehenderit in voluptate velit esse cillum dolore eu fugiat nulla pariatur. Excepteur sint occaecat cupidatat non proident, sunt in culpa qui officia deserunt mollit anim id est laborum.</p>
  <div class="abs btn-pill">READ MORE</div>
  <div class="abs deliv-photo" role="img" aria-label="Candidate in a business meeting with colleagues at a laptop"></div>

  <section class="abs news">
    <p class="kicker">Stay upto date</p>
    <h2>Subscribe to Our Newsletter</h2>
    <div class="pill" style="left:505px;width:219px">Name</div>
    <div class="pill" style="left:734px;width:218px">Email</div>
    <div class="sub">SUBSCRIBE</div>
  </section>

  <footer class="abs footer">
    <div class="abs foot-logo">Daniel Pruitt<small>for Harlow County</small></div>
    <nav class="abs foot-nav">
      <a href="#">Home</a><a href="#">Meet Pruitt</a><a href="#">Endorse</a><a href="#">News</a><a href="#">Volunteer</a>
    </nav>
    <div class="abs socials" aria-label="Social links"><span></span><span></span><span></span></div>
    <div class="abs paid">PAID FOR BY DANIEL PRUITT CAMPAIGN</div>
    <p class="abs fine" style="top:460px">By providing your phone number, you are consenting to receive calls and SMS/MMS messages, including autodialed and automated calls and texts, to that number from the Brennick Ovale campaign. Msg &amp; data rates may apply. Terms &amp; conditions/privacy policies apply. Mobile terms / privacy policy</p>
    <p class="abs fine" style="top:508px">The appearance of candidate in military uniform does not imply or constitute endorsement by the armed services or any federal agency.</p>
  </footer>

</div>
</body>
</html>
```